Vesprine Oakville Cabernet Sauvignon-Wine label design

We need a package design for an up market wine brand named, Vesprine. It will be a Cabernet Sauvignon from the Oakville AVA of Napa Valley. We are looking for a stylish modern label that will stand out on a retail shelf. We want the label to be attention grabbing and stylish while presenting an up market luxury brand.

Sick

Requirements
Must have
• Must have the words(in order of importance)
-Vesprine
-Cabernet Sauvignon
-Oakville
-Napa Valley
-2018

Must be designed for a traditional "Bordeaux" style bottle (Bottle specs in uploaded files)
Should not have
• Any images of grapes, vineyards, wine glasses or bottles

```html
<!DOCTYPE html>
<html lang="en">
<head>
<meta charset="utf-8">
<title>Vesprine Cabernet Sauvignon – Label</title>
<link href="https://fonts.googleapis.com/css2?family=Mrs+Saint+Delafield&family=Source+Sans+3:wght@300;500&display=swap" rel="stylesheet">
<style>
  :root {
    --backdrop: #a6a6a6;
    --label-black: #0a0a0a;
    --leaf-grey: #242424;
    --leaf-soft: #1a1a1a;
    --ink-silver: #dcdcdc;
    --ink-white: #ececec;
  }
  html, body {
    margin: 0;
    padding: 0;
    width: 1200px;
    height: 1189px;
    overflow: hidden;
    background: var(--backdrop);
  }
  .canvas {
    position: relative;
    width: 1200px;
    height: 1189px;
  }
  .wine-label {
    position: absolute;
    left: 376px;
    top: 132px;
    width: 447px;
    height: 924px;
    background: var(--label-black);
    overflow: hidden;
  }
  .leaf-pattern {
    position: absolute;
    inset: 0;
    background:
      radial-gradient(ellipse at 20% 15%, var(--leaf-grey) 0%, transparent 45%),
      radial-gradient(ellipse at 80% 40%, var(--leaf-grey) 0%, transparent 45%),
      radial-gradient(ellipse at 30% 70%, var(--leaf-grey) 0%, transparent 45%),
      radial-gradient(ellipse at 75% 90%, var(--leaf-grey) 0%, transparent 45%),
      var(--leaf-soft);
    opacity: 0.9;
  }
  .label-text {
    position: absolute;
    left: 0;
    width: 100%;
    text-align: center;
    margin: 0;
  }
  .brand-name {
    top: 290px;
    font-family: "Mrs Saint Delafield", cursive;
    font-weight: 400;
    font-size: 120px;
    line-height: 1;
    color: var(--ink-silver);
    letter-spacing: 2px;
  }
  .varietal {
    top: 414px;
    font-family: "Source Sans 3", sans-serif;
    font-weight: 500;
    font-size: 25px;
    color: var(--ink-white);
  }
  .vintage {
    top: 534px;
    font-family: "Source Sans 3", sans-serif;
    font-weight: 300;
    font-size: 40px;
    color: var(--ink-white);
  }
  .appellation {
    top: 684px;
    font-family: "Source Sans 3", sans-serif;
    font-weight: 500;
    font-size: 27px;
    line-height: 40px;
    color: var(--ink-white);
  }
</style>
</head>
<body>
  <main class="canvas">
    <section class="wine-label">
      <div class="leaf-pattern" role="img" aria-label="Tonal pattern of overlapping ginkgo leaves outlined in dark grey on black"></div>
      <h1 class="label-text brand-name">Vesprine</h1>
      <p class="label-text varietal">Cabernet Sauvignon</p>
      <p class="label-text vintage">2018</p>
      <p class="label-text appellation">Oakville<br>Napa Valley</p>
    </section>
  </main>
</body>
</html>
```